Business Card, Stationary with Shark Logo for Personal Injury Lawyer

I need business cards and stationery with a shark logo for my Personal Injury Law Practice. Has to have this written on it:
Martin K. Holloway
Injury Lawyer
The Copperfield Building
718 Wexley Street
Providence, Rhode Island 02908
401-555-0172
Martinholloway.example

Contact Information for Business Card

Martin K. Holloway, Injury Lawyer, address, 401-555-0172, martinholloway.example

```html
<!DOCTYPE html>
<html lang="en">
<head>
<meta charset="utf-8">
<title>Martin K. Holloway – Business Card</title>
<link href="https://fonts.googleapis.com/css2?family=Montserrat:wght@300;400;500;600;800&display=swap" rel="stylesheet">
<style>
  :root {
    --page-bg: #e9e8ec;
    --navy: #39367f;
    --white: #ffffff;
    --ring-grey: #b4b4b8;
    --logo-navy: #2f2b7a;
  }
  html, body {
    margin: 0;
    padding: 0;
    width: 1200px;
    height: 936px;
    overflow: hidden;
    background: var(--page-bg);
    font-family: "Montserrat", Arial, sans-serif;
  }
  .canvas {
    position: relative;
    width: 1200px;
    height: 936px;
  }
  .business-card {
    position: absolute;
    left: 100px;
    top: 182px;
    width: 1000px;
    height: 572px;
    overflow: hidden;
    background: var(--navy);
    box-shadow: 0 10px 28px rgba(0,0,0,0.18);
  }
  .card-shapes {
    position: absolute;
    inset: 0;
  }
  .contact-block {
    position: absolute;
    left: 62px;
    top: 62px;
    color: var(--white);
  }
  .holder-name {
    margin: 0;
    font-size: 33px;
    font-weight: 500;
    letter-spacing: 0.5px;
    text-transform: uppercase;
    line-height: 1.1;
  }
  .holder-title {
    margin: 4px 0 0;
    font-size: 20px;
    font-weight: 300;
    letter-spacing: 1px;
    text-transform: uppercase;
  }
  .office-address {
    margin: 30px 0 0;
    font-style: normal;
    font-size: 21px;
    font-weight: 400;
    line-height: 1.35;
  }
  .building-name {
    display: block;
    font-weight: 600;
    text-transform: uppercase;
  }
  .contact-list {
    list-style: none;
    margin: 26px 0 0;
    padding: 0;
    font-size: 21px;
    line-height: 1.45;
  }
  .contact-list li {
    display: flex;
    align-items: center;
    gap: 10px;
  }
  .contact-icon {
    width: 15px;
    height: 15px;
    flex: none;
  }
  .brand-mark {
    position: absolute;
    left: 540px;
    top: 225px;
    width: 440px;
    text-align: center;
    color: var(--logo-navy);
    font-size: 54px;
    font-weight: 800;
    line-height: 1.0;
    text-transform: uppercase;
    letter-spacing: 1px;
  }
</style>
</head>
<body>
<main class="canvas">
  <section class="business-card" aria-label="Business card">
    <svg class="card-shapes" width="1000" height="572" viewBox="0 0 1000 572" aria-hidden="true">
      <circle class="accent-ring" cx="792" cy="338" r="322" fill="var(--ring-grey)"/>
      <circle class="logo-disc" cx="806" cy="344" r="314" fill="var(--white)"/>
    </svg>

    <div class="contact-block">
      <h1 class="holder-name">Martin K. Holloway</h1>
      <p class="holder-title">Injury Lawyer</p>
      <address class="office-address">
        <span class="building-name">The Copperfield Building</span>
        718 Wexley Street Providence,<br>
        Rhode Island 02908
      </address>
      <ul class="contact-list">
        <li>
          <svg class="contact-icon" viewBox="0 0 16 16" aria-hidden="true"><path d="M4 1.5c.6 0 1 .3 1.2.8l.9 2.4c.2.5 0 1-.4 1.3l-1 .8c.8 1.7 2 2.9 3.6 3.7l.8-1c.3-.4.8-.6 1.3-.4l2.4.9c.5.2.8.6.8 1.2v1.6c0 .8-.7 1.5-1.5 1.4C6.5 13.8 2.2 9.5 1.8 3c0-.8.6-1.5 1.4-1.5z" fill="var(--white)"/></svg>
          <span>401-555-0172</span>
        </li>
        <li>
          <svg class="contact-icon" viewBox="0 0 16 16" aria-hidden="true"><rect x="1.5" y="3.5" width="13" height="9" fill="none" stroke="var(--white)" stroke-width="1.4"/><path d="M1.5 3.5 8 9l6.5-5.5" fill="none" stroke="var(--white)" stroke-width="1.4"/></svg>
          <span>info@martinholloway.example</span>
        </li>
        <li>
          <svg class="contact-icon" viewBox="0 0 16 16" aria-hidden="true"><circle cx="8" cy="8" r="6.3" fill="none" stroke="var(--white)" stroke-width="1.3"/><ellipse cx="8" cy="8" rx="2.7" ry="6.3" fill="none" stroke="var(--white)" stroke-width="1.1"/><path d="M1.7 8h12.6M2.8 4.8h10.4M2.8 11.2h10.4" stroke="var(--white)" stroke-width="1"/></svg>
          <span>www.martinholloway.example</span>
        </li>
      </ul>
    </div>

    <p class="brand-mark">Martin K.<br>Holloway</p>
  </section>
</main>
</body>
</html>
```